Ecommerce Website For Printing Company

Quillbarn.com are a print, design and signage company who sell flyers, business cards, posters, brochures and more to customers in the UK.

Our website is outdated and requires a new design using current web styling and mobile functionality.

We require the following pages to be designed;
- Home Page
- Price Page
- Portfolio Page
- Blog
- Content Page

Our competitors in the printing industry are www.tavenink.com, www.marlowpress.co.uk, brightquire.co.uk, www.leafcrate.co.uk

We require the website to give a professional image as well as be easy for customers to navigate, understand and find prices.

Target Market(s)

Businesses

Industry/Entity Type

Printing

Number of Pages Required

4 page

Font styles to use
Sans Serif

Colors
33a6d7

Requirements
Must have
• Popular products, latest news/blog, sales from portfolio, newsletter sign up, footer

```html
<!DOCTYPE html>
<html lang="en">
<head>
<meta charset="utf-8">
<title>Quillbarn.com – Print, Design &amp; Signage</title>
<link rel="stylesheet" href="https://fonts.googleapis.com/css2?family=Open+Sans:wght@400;600;700;800&display=swap">
<style>
:root{
  --blue:#33a6d7;
  --blue-dark:#2385b0;
  --ink:#222;
  --text:#555;
  --muted:#999;
  --line:#e2e2e2;
  --nav:#1d1d1d;
  --footer:#242424;
  --footer-deep:#181818;
  --red:#e2372d;
  --paper:#fff;
  --soft:#f3f3f3;
}
*{box-sizing:border-box;margin:0;padding:0}
html,body{width:1200px;height:2692px;overflow:hidden}
body{font-family:"Open Sans",Arial,sans-serif;color:var(--text);background:var(--paper);font-size:13px;position:relative}
a{color:inherit;text-decoration:none}
.abs{position:absolute}

/* top bar */
.topbar{position:absolute;left:0;top:0;width:1200px;height:40px;border-bottom:1px solid var(--line);background:#fafafa}
.topbar .phone{position:absolute;left:48px;top:11px;font-size:13px;color:var(--ink);font-weight:600;display:flex;align-items:center;gap:8px}
.topbar .links{position:absolute;right:150px;top:12px;font-size:11px;color:var(--text);letter-spacing:.3px}
.topbar .links span{margin:0 8px;color:#bbb}
.topbar .checkout{position:absolute;right:48px;top:6px;width:90px;height:28px;background:var(--blue);color:#fff;font-size:11px;font-weight:700;text-align:center;line-height:28px}

/* header */
.header{position:absolute;left:0;top:40px;width:1200px;height:112px}
.brand{position:absolute;left:48px;top:34px;display:flex;align-items:center;gap:10px;font-size:34px;font-weight:700;color:var(--blue);letter-spacing:-.5px}
.brand .mark{width:16px;height:16px;background:var(--blue);border-radius:50%}
.brand .tag{font-size:10px;color:var(--ink);font-weight:700;line-height:12px;letter-spacing:.5px;margin-left:6px}
.search{position:absolute;left:470px;top:46px;width:400px;height:34px;border:1px solid var(--line);display:flex}
.search input{flex:1;border:0;padding:0 12px;font:12px "Open Sans",sans-serif;color:var(--muted)}
.search button{width:84px;border:0;background:var(--ink);color:#fff;font:700 11px "Open Sans",sans-serif}
.cart{position:absolute;right:48px;top:50px;display:flex;align-items:center;gap:8px;font-size:12px;color:var(--ink)}
.cart .count{color:var(--blue);font-weight:700}
.cart .btn{border:1px solid var(--line);padding:3px 8px;font-size:11px}

/* nav */
.nav{position:absolute;left:0;top:156px;width:1200px;height:46px;background:var(--nav);display:flex;padding-left:48px}
.nav a{color:#fff;font-size:11px;font-weight:700;letter-spacing:.3px;line-height:46px;padding:0 18px}
.nav a.home{background:var(--blue);width:60px;padding:0;display:flex;align-items:center;justify-content:center}
.nav a.active-sub{color:#fff}

/* hero */
.hero{position:absolute;left:0;top:206px;width:1200px;height:510px;background:linear-gradient(#eceff2,#d9dde2)}
.hero h1{position:absolute;left:160px;top:60px;font-size:60px;line-height:60px;font-weight:800;color:#2a2a2a;letter-spacing:-1px;text-shadow:0 2px 0 rgba(255,255,255,.6)}
.hero .visual{position:absolute;left:150px;top:30px;width:890px;height:430px;border-radius:4px;background:linear-gradient(120deg,#cfd7df 0%,#f1c98e 45%,#e8573f 60%,#7fb6d9 80%,#d4d9de 100%);opacity:.85}
.hero .caption{position:absolute;left:46px;top:400px;font-size:18px;color:#333}
.hero .caption a{color:var(--blue);font-weight:600}
.hero .dots{position:absolute;right:50px;top:456px;display:flex;gap:8px}
.hero .dots i{width:12px;height:12px;border-radius:50%;background:#fff;display:block}
.hero .dots i.on{background:var(--blue)}

/* features */
.features{position:absolute;left:48px;top:770px;width:1104px;height:96px;display:flex;justify-content:space-between;border-bottom:1px solid var(--line)}
.feature{display:flex;align-items:center;gap:12px;width:240px}
.feature .icon{width:48px;height:48px;border-radius:4px;background:#eef6fb;display:flex;align-items:center;justify-content:center}
.feature h3{font-size:16px;color:var(--blue);font-weight:700;letter-spacing:.5px}
.feature p{font-size:11px;color:var(--muted)}

/* sidebar */
.side-box{position:absolute;left:48px;width:264px;border:1px solid var(--line)}
.side-box h4{background:var(--ink);color:#fff;font-size:11px;font-weight:700;padding:11px 14px;letter-spacing:.3px}
.cat-list{list-style:none}
.cat-list li{font-size:11px;padding:0 14px;height:37px;line-height:37px;border-bottom:1px solid #eee;color:var(--text)}
.cat-list li::before{content:"›";margin-right:8px;color:var(--muted)}
.cat-list li.current{background:var(--blue);color:#fff}
.cat-list li.current::before{color:#fff}
.news-item{padding:12px 14px 4px}
.news-item h5{font-size:11px;color:var(--ink);font-weight:800}
.news-item p{font-size:11px;color:var(--blue);line-height:15px}
.more{display:block;text-align:right;font-size:11px;color:var(--blue);padding:6px 14px 12px}
.blog-row{display:flex;gap:12px;padding:14px}
.avatar{width:52px;height:52px;flex:none;background:linear-gradient(#c9d3dc,#9aa8b4);border-radius:2px}
.blog-row p{font-size:11px;line-height:15px;color:var(--text)}

/* section headings */
.sec-title{position:absolute;font-size:22px;font-weight:700;color:var(--blue);letter-spacing:.3px}
.sec-title b{color:var(--ink);font-weight:700}
.sec-rule{position:absolute;height:1px;background:var(--line)}
.sort{position:absolute;left:1090px;top:924px;border:1px solid var(--line);font-size:10px;padding:4px 8px;color:var(--ink)}

/* product cards */
.product{position:absolute;width:400px;height:200px;border:1px solid var(--line);background:#fff}
.product.featured{background:var(--blue);border-color:var(--blue)}
.product .thumb{position:absolute;left:14px;top:30px;width:180px;height:140px;background:linear-gradient(135deg,#dfe3e7,#b9c2ca)}
.product.featured .thumb{background:linear-gradient(135deg,#e9f4fa,#9ccfe8)}
.product .dark .thumb{}
.product h3{position:absolute;left:210px;top:40px;font-size:17px;font-weight:600;color:var(--ink)}
.product.featured h3,.product.featured p{color:#fff}
.product p{position:absolute;left:210px;top:68px;width:170px;font-size:10px;line-height:14px;color:var(--text)}
.product .read{position:absolute;left:210px;top:140px;width:86px;height:24px;border:1px solid var(--line);font-size:9px;font-weight:700;color:var(--blue);text-align:center;line-height:22px;background:#fff}

/* portfolio */
.sale-card{position:absolute;width:252px;height:368px;border:1px solid var(--line);background:#fff}
.sale-card.featured{background:#d7eef8;border-color:var(--blue)}
.sale-card .thumb{position:absolute;left:16px;top:14px;width:220px;height:200px;background:linear-gradient(135deg,#3a3d42,#f1d335 60%,#e0e3e6)}
.sale-card .tag{position:absolute;left:0;top:0;background:var(--red);color:#fff;font-size:10px;font-weight:700;padding:3px 7px}
.sale-card h3{position:absolute;left:0;top:236px;width:100%;text-align:center;font-size:11px;font-weight:800;color:var(--ink)}
.sale-card.featured h3{color:var(--blue)}
.sale-card .price{position:absolute;left:0;top:262px;width:100%;text-align:center;font-size:22px;color:var(--ink);font-weight:600}
.sale-card .price s{font-size:12px;color:var(--muted);margin-right:6px;font-weight:400}
.sale-card .actions{position:absolute;left:20px;top:310px;display:flex;gap:10px}
.sale-card .actions span{width:40px;height:40px;border-radius:50%;border:1px solid var(--line);background:#fff;display:flex;align-items:center;justify-content:center}
.sale-card .actions span.cart-btn{border-radius:2px;background:var(--ink);border-color:var(--ink)}
.sale-card.featured .actions span.cart-btn{background:var(--blue);border-color:var(--blue)}

/* newsletter */
.newsletter{position:absolute;left:0;top:1946px;width:1200px;height:234px;background:var(--blue);color:#fff}
.newsletter h2{position:absolute;left:48px;top:60px;font-size:40px;font-weight:400}
.newsletter p{position:absolute;left:48px;top:116px;width:390px;font-size:11px;line-height:15px;color:#e4f4fb}
.newsletter .field{position:absolute;left:528px;top:64px;width:236px;height:34px;background:#fff;color:var(--muted);font-size:11px;line-height:34px;padding-left:12px}
.newsletter .subscribe{position:absolute;left:528px;top:108px;width:236px;height:34px;background:var(--ink);font-size:11px;font-weight:700;line-height:34px;text-align:center}
.newsletter .ship{position:absolute;left:880px;top:58px;display:flex;gap:16px;align-items:center}
.newsletter .ship h3{font-size:38px;line-height:38px;font-weight:800}
.newsletter .ship small{font-size:12px;color:#e4f4fb}

/* social */
.follow{position:absolute;left:0;top:2180px;width:1200px;height:200px;background:#f6f6f6;text-align:center}
.follow h2{margin-top:28px;font-size:20px;font-weight:700;color:var(--blue);letter-spacing:.5px}
.socials{position:absolute;top:90px;left:220px;display:flex;gap:60px}
.social{width:220px}
.social a{display:block;height:52px;line-height:52px;color:#fff;font-size:20px;font-weight:700}
.social small{display:block;margin-top:10px;font-size:11px;color:var(--muted)}
.s-face a{background:#3b5a9a}
.s-chirp a{background:#2fb0e6}
.s-work a{background:#2a6f8e}

/* footer */
.footer{position:absolute;left:0;top:2380px;width:1200px;height:280px;background:var(--footer);color:#aaa}
.fcol{position:absolute;top:22px;width:240px}
.fcol h4{color:#fff;font-size:11px;font-weight:700;letter-spacing:.5px;margin-bottom:14px}
.fcol li{list-style:none;font-size:10px;line-height:19px;text-transform:uppercase}
.contact-line{display:flex;gap:8px;align-items:flex-start;font-size:10px;line-height:16px;margin-bottom:8px}
.cards{display:flex;gap:6px;margin-top:10px}
.cards i{width:34px;height:22px;background:#555;border-radius:3px;display:block}
.bottom{position:absolute;left:0;top:2660px;width:1200px;height:32px;background:var(--footer-deep);color:#888;font-size:10px;line-height:32px;padding-left:48px}
</style>
</head>
<body>

<div class="topbar">
  <div class="phone">
    <svg width="14" height="14" viewBox="0 0 24 24"><path fill="#33a6d7" d="M6.6 10.8a15 15 0 0 0 6.6 6.6l2.2-2.2c.3-.3.7-.4 1-.2 1.1.4 2.3.6 3.6.6.6 0 1 .4 1 1V20c0 .6-.4 1-1 1A17 17 0 0 1 3 4c0-.6.4-1 1-1h3.5c.6 0 1 .4 1 1 0 1.3.2 2.5.6 3.6.1.3 0 .7-.2 1z"/></svg>
    01632 960 418
  </div>
  <div class="links">CUSTOMER SERVICE<span>|</span>MY ACCOUNT<span>|</span>WISHLIST</div>
  <a class="checkout" href="#">CHECKOUT ›</a>
</div>

<header class="header">
  <div class="brand"><span class="mark"></span>Quillbarn.com<span class="tag">PRINT<br>DESIGN<br>SIGNAGE</span></div>
  <div class="search"><input value="Enter search..." aria-label="Search"><button>SEARCH</button></div>
  <div class="cart">
    <svg width="18" height="16" viewBox="0 0 24 20"><path fill="none" stroke="#222" stroke-width="2" d="M1 1h4l3 12h12l3-9H6"/><circle cx="9" cy="17" r="2" fill="#222"/><circle cx="19" cy="17" r="2" fill="#222"/></svg>
    CART <span class="count">(0)</span> £0.00 <span class="btn">▾</span>
  </div>
</header>

<nav class="nav">
  <a class="home" href="#"><svg width="18" height="16" viewBox="0 0 24 22"><path fill="#fff" d="M12 1 1 11h3v10h6v-6h4v6h6V11h3z"/></svg></a>
  <a href="#">ABOUT</a><a href="#">PRINTING</a><a href="#">GRAPHIC DESIGN</a><a href="#">WEBSITE DESIGN</a><a href="#">ARTWORK GUIDE</a><a href="#">SAMPLE PACK</a><a href="#">UPLOAD</a><a href="#">TESTIMONIALS</a><a href="#">BLOG</a><a href="#">CONTACT US</a>
</nav>

<section class="hero">
  <div class="visual" role="img" aria-label="Printed sticker, label and brochure samples fanned out"></div>
  <h1 style="left:46px;top:232px">STICKER &amp;<br>LABEL PRINTING</h1>
  <p class="caption">Many sizes available, <a href="#">click here</a> for more details</p>
  <div class="dots"><i class="on"></i><i></i><i></i></div>
</section>

<section class="features">
  <div class="feature"><div class="icon"><svg width="26" height="26" viewBox="0 0 24 24"><path fill="#33a6d7" d="M2 10h4v12H2zM8 22h10c1 0 1.7-.6 2-1.5l2-7c.3-1-.5-2-1.5-2H15l1-5c.2-1-.6-2-1.6-2L8 10z"/></svg></div><div><h3>SATISFACTION</h3><p>100% Guaranteed</p></div></div>
  <div class="feature"><div class="icon"><svg width="28" height="22" viewBox="0 0 28 20"><path fill="#33a6d7" d="M1 2h16v12H1zM18 6h5l4 4v4h-9z"/><circle cx="6" cy="16" r="3" fill="#33a6d7"/><circle cx="22" cy="16" r="3" fill="#33a6d7"/></svg></div><div><h3>FREE SHIPPING</h3><p>on orders over $99</p></div></div>
  <div class="feature"><div class="icon"><svg width="26" height="26" viewBox="0 0 24 24"><rect x="2" y="4" width="20" height="18" rx="2" fill="none" stroke="#33a6d7" stroke-width="2"/><path d="M2 9h20M7 2v4M17 2v4" stroke="#33a6d7" stroke-width="2"/></svg></div><div><h3>7 DAY</h3><p>Easy  to Return Items</p></div></div>
  <div class="feature"><div class="icon"><svg width="26" height="26" viewBox="0 0 24 24"><path fill="none" stroke="#33a6d7" stroke-width="2" d="M4 14v-3a8 8 0 0 1 16 0v3"/><rect x="2" y="13" width="5" height="7" rx="1" fill="#33a6d7"/><rect x="17" y="13" width="5" height="7" rx="1" fill="#33a6d7"/></svg></div><div><h3>SUPPORT</h3><p>Customer Service</p></div></div>
</section>

<aside>
  <div class="side-box" style="top:920px">
    <h4>POPULAR PRODUCTS</h4>
    <ul class="cat-list">
      <li>Flyer Printing</li><li>Leaflet Flyers</li><li>Brochure Printing</li><li class="current">Poster Printing</li><li>Banner Printing</li><li>Letterhead Printing</li><li>Compliment Slips</li><li>Folding Services</li><li>Invoice Pads &amp; NCR Pads</li><li>Stickers and Labels</li><li>Presentation folders</li><li>Christmas cards</li>
    </ul>
  </div>
  <div class="side-box" style="top:1430px">
    <h4>LATEST NEWS</h4>
    <div class="news-item"><h5>LOREM IPSUM DOLOR SIT AMET</h5><p>New paper stock added to our flyer and poster ranges</p></div>
    <div class="news-item"><h5>LOREM IPSUM DOLOR SIT AMET</h5><p>Next-day delivery now on all business card orders</p></div>
    <a class="more" href="#">More News</a>
  </div>
  <div class="side-box" style="top:1702px">
    <h4>LATEST BLOG</h4>
    <div class="blog-row"><div class="avatar" role="img" aria-label="Author portrait"></div><p>We have just completed a new set of brochures for a local business client.<br><a href="#" style="color:var(--blue)">Read Blog Entry</a></p></div>
  </div>
</aside>

<h2 class="sec-title" style="left:352px;top:918px">POPULAR <b>PRODUCTS</b></h2>
<div class="sort">SORT BY ▾</div>
<div class="sec-rule" style="left:352px;top:958px;width:800px"></div>

<article class="product featured" style="left:352px;top:980px">
  <div class="thumb" role="img" aria-label="Stack of printed business cards"></div>
  <h3>Business Cards</h3><p>Sharp full colour cards on thick stock, printed and shipped fast.</p><a class="read" href="#">READ MORE</a>
</article>
<article class="product" style="left:752px;top:980px">
  <div class="thumb" role="img" aria-label="Printed A4 letterhead sheets"></div>
  <h3>A4 Letterheads</h3><p>Branded letterheads on premium paper for every office need.</p><a class="read" href="#">READ MORE</a>
</article>
<article class="product" style="left:352px;top:1200px">
  <div class="thumb" role="img" aria-label="Printed A5 flyers" style="background:linear-gradient(135deg,#2c2f33,#e9d332)"></div>
  <h3>A5 Flyers</h3><p>Bright gloss or silk flyers ideal for events and promotions.</p><a class="read" href="#">READ MORE</a>
</article>
<article class="product" style="left:752px;top:1200px">
  <div class="thumb" role="img" aria-label="Printed A6 flyers" style="background:linear-gradient(135deg,#2c2f33,#e9d332)"></div>
  <h3>A6 Flyers</h3><p>Compact flyers for handouts, vouchers and mail drops.</p><a class="read" href="#">READ MORE</a>
</article>

<h2 class="sec-title" style="left:352px;top:1460px">SALES <b>FROM PORTFOLIO</b></h2>
<div class="sec-rule" style="left:600px;top:1476px;width:552px"></div>

<article class="sale-card" style="left:352px;top:1512px">
  <div class="thumb" role="img" aria-label="Printed flyer product sample"></div><span class="tag">SALE</span>
  <h3>NAME OF THE PRODUCT</h3><div class="price"><s>$39.00</s>$ 29.00</div>
  <div class="actions"><span class="cart-btn"><svg width="16" height="14" viewBox="0 0 24 20"><path fill="none" stroke="#fff" stroke-width="2.5" d="M1 1h4l3 12h12l3-9H6"/></svg></span><span>♡</span><span>⇄</span><span>✎</span></div>
</article>
<article class="sale-card featured" style="left:626px;top:1512px">
  <div class="thumb" role="img" aria-label="Printed flyer product sample"></div><span class="tag">SALE</span>
  <h3>NAME OF THE PRODUCT</h3><div class="price"><s>$39.00</s>$ 29.00</div>
  <div class="actions"><span class="cart-btn"><svg width="16" height="14" viewBox="0 0 24 20"><path fill="none" stroke="#fff" stroke-width="2.5" d="M1 1h4l3 12h12l3-9H6"/></svg></span><span>♡</span><span>⇄</span><span>✎</span></div>
</article>
<article class="sale-card" style="left:900px;top:1512px">
  <div class="thumb" role="img" aria-label="Printed flyer product sample"></div><span class="tag">SALE</span>
  <h3>NAME OF THE PRODUCT</h3><div class="price"><s>$39.00</s>$ 29.00</div>
  <div class="actions"><span class="cart-btn"><svg width="16" height="14" viewBox="0 0 24 20"><path fill="none" stroke="#fff" stroke-width="2.5" d="M1 1h4l3 12h12l3-9H6"/></svg></span><span>♡</span><span>⇄</span><span>✎</span></div>
</article>

<section class="newsletter">
  <h2>Newsletter Sign Up</h2>
  <p>Join our mailing list for print offers, new product news and seasonal discounts sent straight to your inbox each month.</p>
  <div class="field">Enter your email address</div>
  <div class="subscribe">SUBSCRIBE</div>
  <div class="ship">
    <svg width="70" height="50" viewBox="0 0 28 20"><path fill="#fff" d="M1 2h16v12H1zM18 6h5l4 4v4h-9z"/><circle cx="6" cy="16" r="3" fill="#fff"/><circle cx="22" cy="16" r="3" fill="#fff"/></svg>
    <div><h3>FREE<br>SHIPPING</h3><small>on orders over $ 99</small></div>
  </div>
</section>

<section class="follow">
  <h2>FOLLOW US TO STAY IN TOUCH</h2>
  <div class="socials">
    <div class="social s-face"><a href="#">Facepage</a><small>12.4K likes</small></div>
    <div class="social s-chirp"><a href="#">Chirper</a><small>3,210 Followers</small></div>
    <div class="social s-work"><a href="#">WorkLinks</a><small>1,056 Connections</small></div>
  </div>
</section>

<footer class="footer">
  <div class="fcol" style="left:48px"><h4>INFORMATION</h4><ul><li>About Us</li><li>Customer Service</li><li>Privacy Policy</li><li>Search Terms</li><li>Orders and Returns</li><li>Contact Us</li></ul></div>
  <div class="fcol" style="left:324px"><h4>WHY BUY FROM US</h4><ul><li>Shipping &amp; Returns</li><li>Secure Shopping</li><li>International Shipping</li><li>Affiliates</li><li>Group Sales</li></ul></div>
  <div class="fcol" style="left:626px"><h4>MY ACCOUNT</h4><ul><li>Sign In</li><li>View Cart</li><li>My Wishlist</li><li>Track My Order</li><li>Help</li></ul></div>
  <div class="fcol" style="left:870px;width:290px"><h4>CONTACTS</h4>
    <div class="contact-line"><svg width="10" height="14" viewBox="0 0 10 14"><path fill="#33a6d7" d="M5 0a5 5 0 0 0-5 5c0 4 5 9 5 9s5-5 5-9a5 5 0 0 0-5-5zm0 7a2 2 0 1 1 0-4 2 2 0 0 1 0 4z"/></svg>12 Mill Lane, Harbour Park, Northbridge NB4 7QT</div>
    <div class="contact-line"><svg width="12" height="12" viewBox="0 0 24 24"><path fill="#33a6d7" d="M6.6 10.8a15 15 0 0 0 6.6 6.6l2.2-2.2c.3-.3.7-.4 1-.2 1.1.4 2.3.6 3.6.6.6 0 1 .4 1 1V20c0 .6-.4 1-1 1A17 17 0 0 1 3 4c0-.6.4-1 1-1h3.5c.6 0 1 .4 1 1 0 1.3.2 2.5.6 3.6.1.3 0 .7-.2 1z"/></svg>TEL: 01632 960 418</div>
    <div class="contact-line"><svg width="12" height="10" viewBox="0 0 24 18"><rect x="1" y="1" width="22" height="16" fill="none" stroke="#33a6d7" stroke-width="2"/><path d="M1 1l11 9 11-9" fill="none" stroke="#33a6d7" stroke-width="2"/></svg>EMAIL: hello@quillbarn.com</div>
    <div class="cards"><i></i><i></i><i></i><i></i></div>
  </div>
</footer>
<div class="bottom">© Rights Reserved. Quillbarn.com 2015</div>

</body>
</html>
```